Chatterly News Feed Advertisement for Bitcoin Startup

CoinHarbor is a bitcoin brokerage in South Africa.
We need an advertisement for our Chatterly newsfeed.
Modern, technology feel to the advertisement.
Colours should compliment our logo in the attached document
Advertisement text: "The cheapest Bitcoin in South Africa"
Creative hints: Include an image of a bitcoin. Include something visual relating to South Africa (map, flag etc.). These are just hints an do not need to be followed to the letter, we appreciate creative freedom.
Updates

Project Deadline Extended Reason: This advertisement will only be needed on 10th May. Added Monday, April 24, 2017

Target Market(s)

People wanting to purchase bitcoin

Industry/Entity Type

News

Font styles to use
Sans Serif

Colors

Designer to choose colors to be used in the design.

Requirements
Must have
• Size: 1000 x 561 pixels (landscape)
• Text must not constitute more than 20% of the design (as per Chatterly requirements0
Nice to have
• Attached is our logo for your reference. Creative freedom is yours.
Should not have
• No preferences

Files

```html
<!DOCTYPE html>
<html lang="en">
<head>
<meta charset="utf-8">
<title>CoinHarbor – The cheapest Bitcoin in South Africa</title>
<link rel="stylesheet" href="https://fonts.googleapis.com/css2?family=Open+Sans:wght@700;800&display=swap">
<style>
  :root {
    --page: #e9e9e9;
    --navy: #1d2b57;
    --orange: #f7a51c;
    --gold-light: #fbe39a;
    --gold-mid: #e2b23c;
    --gold-deep: #9c6a0e;
    --gold-dark: #5e3d05;
  }
  html, body {
    margin: 0;
    width: 1200px;
    height: 960px;
    overflow: hidden;
    background: var(--page);
  }
  .ad {
    position: absolute;
    left: 40px;
    top: 168px;
    width: 1120px;
    height: 624px;
    overflow: hidden;
    font-family: "Open Sans", Arial, sans-serif;
  }
  .ad__photo {
    position: absolute;
    inset: 0;
    background:
      radial-gradient(circle at 700px 312px, var(--gold-light) 0, var(--gold-mid) 150px, var(--gold-deep) 260px, transparent 280px),
      radial-gradient(ellipse at 230px 380px, rgba(255,244,200,.85) 0, rgba(240,190,80,.5) 180px, transparent 340px),
      linear-gradient(100deg, var(--gold-dark) 0%, var(--gold-deep) 30%, var(--gold-mid) 55%, var(--gold-light) 85%, var(--gold-mid) 100%);
  }
  .brand {
    position: absolute;
    left: 80px;
    top: 58px;
    display: flex;
    align-items: center;
    gap: 16px;
    color: var(--navy);
    font-weight: 700;
    font-size: 50px;
    letter-spacing: -0.5px;
  }
  .brand__mark {
    width: 46px;
    height: 46px;
    border-radius: 50%;
    background: var(--navy);
  }
  .headline {
    position: absolute;
    left: 80px;
    top: 240px;
    margin: 0;
    font-weight: 800;
    line-height: 1.12;
    color: var(--navy);
  }
  .headline__line { display: block; font-size: 56px; }
  .headline__line--bitcoin { font-size: 58px; }
  .headline__line--country {
    margin-top: 14px;
    font-size: 64px;
    color: var(--orange);
    -webkit-text-stroke: 2px var(--navy);
    paint-order: stroke fill;
    text-shadow: 0 3px 6px rgba(0,0,0,.25);
  }
</style>
</head>
<body>
  <main class="ad">
    <div class="ad__photo" role="img" aria-label="Photograph of a gold bitcoin coin standing in front of blurred stacks of gold coins"></div>
    <div class="brand">
      <span class="brand__mark"></span>
      <span class="brand__name">CoinHarbor</span>
    </div>
    <h1 class="headline">
      <span class="headline__line">THE</span>
      <span class="headline__line">CHEAPEST</span>
      <span class="headline__line headline__line--bitcoin">Bitcoin in</span>
      <span class="headline__line headline__line--country">SOUTH AFRICA</span>
    </h1>
  </main>
</body>
</html>
```